Design a sleek menu for our new smoothie and snacks shop”Zest”

requiring a store drinks and snacks menu we would like to have a white background for the menu . I would like to have fruit watermarks like in our original design concept , For reference ,please refer to the pictures . The font and layout of the menu should be modern , simple but stylish and reflect a smoothie shop.
we will be proving the menu contents to input once we agree to the design concept .
here are the menu documents

smoothies

Regular 16oz £4.99 Large 20oz £5.99
substitute semi skim for any dairy free milks for .50p
add vegan protein or regular protein for .50p

Berry set go
mixed berries, banana, coconut yogurt, milk

Green Machine
Spinach, avocado, matcha, banana, milk, agave

Power to the purple
Blueberries, banana, açai, coconut milk

Mango Monsoon
Mango, apple, strawberry, coconut milk, vanilla yogurt, agave

Go Bear Zest
Oats, banana, cinnamon, dates, almond butter

Caribbean Dream
Pineapple, spinach, banana, coconut milk

Mocha lotta
Oats, banana, cinnamon, cocoa, espresso, skim milk

Cocoa Banana
Oats, banana, cocoa, cinnamon, peanut butter , agave
*almond butter substitute is available

PB & J Day
Frozen berries, banana, peanut butter, maple syrup, coconut milk
*Spinach is optional

Strawberry Zest
Strawberries, banana, coconut milk, orange juice, agave

Kale Krush
Spinach, kale, pineapple, apple juice

Young Blood
Celery, lemon, apple

Berry Beautiful
Blueberries, banana, vanilla yogurt, soy milk, collagen protein, agave,

Shakes
Large 16oz £6
Add Protein for .50p

Avo Shake
Avocado, banana, skim milk, vanilla

Cocoa Shake
Avocado, cocoa powder, coconut milk, banana, maple syrup
*can substitute avocado with dairy free ice cream

Sweet Vegan
Dairy free vanilla Ice cream, banana, cocoa powder, coconut milk, agave

The last straw
Strawberry ,dates , dairy free ice cream, coconut milk, agave
*substitute dairy free ice cream for avocado

Caffeine frenzy
Espresso, banana, dairy free ice cream, cocoa powder, almond milk, agave

Berry Bunch
Oats, mixed berries, banana, dates ,soy milk, dairy free ice cream

Immune boosters
Regular 16 oz £6
Smoothie Bowl £5.50 * Available on a seasonal basis

The yellow one: Pineapple turmeric
Pineapple, banana, lemon, agave, ginger,tumeric,coconut water

The Red one : Citrus Berry Ginger
Orange, strawberry, lemon, ginger , almond milk

The Orange one : Citrus carrot
Grapefruit, clementine, carrot,mango,yogurt,lemon,tumeric

Teas
Regular £2
Green geisha
Breakfast blend
Lemon & ginger
Moroccan mint

Iced Frappucino
* Substitute for non dairy for .50p
Regular £3.50
Cappuccino - expresso, milk, ice
Mocha- cocoa ,milk, ice
Strawberry's n cream- Strawberry,cream,ice
Mighty Matcha - Matcha, cream, ice
Vanilla Bean- Vanilla, cream, ice
Zest Sandwiches
£4.50

Avocado
Avocado , mozerella,tomatoe, pesto

Spicy Tuna
Tuna, Chilli peppers, mayo, salt, pepper

Tunacado
Tuna, avocado, mayo, salt, pepper

BLT
Turkey Rasher, lettuce, mayo, tomatoe

American Grilled Cheese
Mature Cheddar , wholewheat bread
*sourdough bread is optional

Yogurt
£3
Coconut ,Vanilla yogurt , banana, granola

Bowls
£4.50
+ protein=.50p

Acai Bowl
Acai, Raspberry,blueberry,banana,almond milk, granola
*Topping: granola and ½ banana sliced ,chia seeds

Cocoa Bowl
Cocoa,banana,peanut butter,almond milk
Toppings : chocolate granola, peanut butter ,chia seeds,1/2 banana sliced

Target Market(s)

any age , predominately ages 20+

Industry/Entity Type

food & drink

Colors

Designer to choose colors to be used in the design.

Requirements
Must have
• clean, modern concept
Nice to have
• white background, fruits in the background -animated or actual ones
Should not have
• no dark background concepts

```html
<!DOCTYPE html>
<html lang="en">
<head>
<meta charset="utf-8">
<title>Zest Menu</title>
<link href="https://fonts.googleapis.com/css2?family=Dosis:wght@400;500&family=Nunito+Sans:wght@400;600&display=swap" rel="stylesheet">
<style>
:root{
  --navy:#1c2535;
  --lime:#9ddc3c;
  --lime-dark:#6fae1f;
  --pink:#e8246b;
  --ink:#1a1a1a;
  --paper:#ffffff;
  --backdrop:#f3f1ee;
}
*{margin:0;padding:0;box-sizing:border-box}
html,body{width:880px;height:1200px;overflow:hidden}
body{background:var(--backdrop);font-family:"Nunito Sans",sans-serif;color:var(--ink);position:relative}
.backdrop-art{position:absolute;inset:0;background:radial-gradient(circle at 10% 20%,#f7dfe3 0,transparent 18%),radial-gradient(circle at 92% 40%,#dde0f5 0,transparent 16%),radial-gradient(circle at 5% 85%,#eef5d8 0,transparent 16%),radial-gradient(circle at 95% 90%,#fbeccf 0,transparent 14%),var(--backdrop)}
.sheet{position:absolute;left:28px;top:28px;width:822px;height:1144px;background:var(--paper);box-shadow:0 2px 10px rgba(0,0,0,.15)}
.fruit{position:absolute;border-radius:50%;opacity:.55}
.brand-tab{position:absolute;left:388px;top:0;width:103px;height:104px;background:var(--navy);display:flex;align-items:center;justify-content:center}
.brand-ring{width:60px;height:60px;border:2px solid #fff;border-radius:50%;display:flex;align-items:center;justify-content:center;color:#fff;font-family:"Dosis",sans-serif;font-size:20px;font-weight:500}
.abs{position:absolute}
.heading{font-family:"Dosis",sans-serif;font-weight:500;font-size:30px;color:var(--lime);letter-spacing:.5px;line-height:1;text-shadow:0 0 1px var(--navy),1px 1px 0 var(--navy)}
.band{position:absolute;background:var(--navy);color:#fff;font-size:13px;line-height:14px;padding:3px 10px}
.band .price{color:var(--lime);font-weight:600;font-family:"Dosis",sans-serif;font-size:14px}
.item{margin-bottom:8px}
.item-name{font-family:"Dosis",sans-serif;font-weight:500;font-size:14px;line-height:13px;text-transform:uppercase;color:var(--navy)}
.item-desc{font-size:12.5px;line-height:12px}
.note{color:var(--pink);font-size:12.5px;line-height:12px}
.right{text-align:right}
.plain-list{font-size:13.5px;line-height:20px;font-weight:600;text-align:right}
.plain-list span{font-weight:400}
.vdash{position:absolute;left:440px;top:160px;height:1010px;border-left:1.5px dashed var(--navy)}
.hdash{position:absolute;border-top:1.5px dashed var(--navy)}
</style>
</head>
<body>
<div class="backdrop-art" role="img" aria-label="Hand-drawn fruit sketches in pink, blue, green and orange around the edges"></div>
<main class="sheet">
  <div class="fruit" role="img" aria-label="Sketched red apple" style="left:360px;top:270px;width:70px;height:70px;background:#f5b9bd"></div>
  <div class="fruit" role="img" aria-label="Sketched bunch of blue grapes" style="left:400px;top:160px;width:80px;height:90px;background:#b7bdea"></div>
  <div class="fruit" role="img" aria-label="Sketched lemon slice" style="left:280px;top:395px;width:70px;height:45px;background:#f3e59a"></div>
  <div class="fruit" role="img" aria-label="Sketched lime half" style="left:338px;top:470px;width:58px;height:50px;background:#c8eeb0"></div>
  <div class="fruit" role="img" aria-label="Sketched kiwi and green apple" style="left:430px;top:360px;width:90px;height:60px;background:#cfe7c0"></div>
  <div class="fruit" role="img" aria-label="Sketched grapes" style="left:430px;top:640px;width:85px;height:80px;background:#b7bdea"></div>
  <div class="fruit" role="img" aria-label="Sketched lime half" style="left:445px;top:745px;width:75px;height:70px;background:#c8eeb0"></div>
  <div class="fruit" role="img" aria-label="Sketched orange" style="left:315px;top:860px;width:70px;height:70px;background:#f4d4a0"></div>
  <div class="fruit" role="img" aria-label="Sketched pineapple" style="left:330px;top:1020px;width:90px;height:120px;background:#e3efc4;border-radius:45%"></div>
  <div class="fruit" role="img" aria-label="Sketched strawberry" style="left:290px;top:590px;width:50px;height:55px;background:#f5b9bd"></div>

  <div class="brand-tab"><div class="brand-ring">Zest</div></div>

  <div class="vdash"></div>
  <div class="hdash" style="left:46px;top:704px;width:350px"></div>
  <div class="hdash" style="left:447px;top:278px;width:340px"></div>
  <div class="hdash" style="left:447px;top:430px;width:340px"></div>
  <div class="hdash" style="left:447px;top:580px;width:340px"></div>
  <div class="hdash" style="left:447px;top:842px;width:340px"></div>
  <div class="hdash" style="left:447px;top:930px;width:340px"></div>
</main>

<h2 class="abs heading" style="left:74px;top:78px">SMOOTHIES</h2>
<div class="band" style="left:0;top:112px;width:438px;padding-left:74px">
  <div class="price">REGULAR 16OZ £4.99 LARGE 20OZ £5.99</div>
  Substitute semi skim for any dairy free milks for .50p<br>add vegan protein or regular protein for .50p
</div>
<section class="abs" style="left:74px;top:179px;width:320px">
  <div class="item"><div class="item-name">Berry Set Go</div><div class="item-desc">mixed berries, banana, coconut yogurt, milk</div></div>
  <div class="item"><div class="item-name">Green Machine</div><div class="item-desc">Spinach, avocado, matcha, banana, milk, agave</div></div>
  <div class="item"><div class="item-name">Power to the Purple</div><div class="item-desc">Blueberries, banana, açai, coconut milk</div></div>
  <div class="item"><div class="item-name">Mango Monsoon</div><div class="item-desc">Mango, apple, strawberry, coconut milk,<br>vanilla yogurt, agave</div></div>
  <div class="item"><div class="item-name">Go Bear Zest</div><div class="item-desc">Oats, banana, cinnamon, dates, almond butter</div></div>
  <div class="item"><div class="item-name">Caribbean Dream</div><div class="item-desc">Pineapple, spinach, banana, coconut milk</div></div>
  <div class="item"><div class="item-name">Mocha Lotta</div><div class="item-desc">Oats, banana, cinnamon, cocoa,<br>espresso, skim milk</div></div>
  <div class="item"><div class="item-name">Cocoa Banana</div><div class="item-desc">Oats, banana, cocoa, cinnamon,<br>peanut butter, agave</div><div class="note">*almond butter substitute is available</div></div>
  <div class="item"><div class="item-name">PB &amp; J Day</div><div class="item-desc">Frozen berries, banana, peanut butter,<br>maple syrup, coconut milk<br>*Spinach is optional</div></div>
  <div class="item"><div class="item-name">Strawberry Zest</div><div class="item-desc">Strawberries, banana, coconut milk,<br>orange juice, agave</div></div>
  <div class="item"><div class="item-name">Kale Krush</div><div class="item-desc">Spinach, kale, pineapple, apple juice</div></div>
  <div class="item"><div class="item-name">Young Blood</div><div class="item-desc">Celery, lemon, apple</div></div>
  <div class="item"><div class="item-name">Berry Beautiful</div><div class="item-desc">Blueberries, banana, vanilla yogurt, soy milk,<br>collagen protein, agave,</div></div>
</section>

<h2 class="abs heading" style="left:74px;top:743px">SHAKES</h2>
<div class="band" style="left:0;top:776px;width:228px;padding-left:76px">
  <div class="price">LARGE 16OZ £6</div>Add Protein for .50p
</div>
<section class="abs" style="left:71px;top:834px;width:300px">
  <div class="item"><div class="item-name">Avo Shake</div><div class="item-desc">Avocado, banana, skim milk, vanilla</div></div>
  <div class="item"><div class="item-name">Cocoa Shake</div><div class="item-desc">Avocado, cocoa powder, coconut milk,<br>banana, maple syrup</div><div class="note">*can substitute avocado with dairy<br>free ice cream</div></div>
  <div class="item"><div class="item-name">Sweet Vegan</div><div class="item-desc">Dairy free vanilla Ice cream, banana,<br>cocoa powder, coconut milk, agave</div></div>
  <div class="item"><div class="item-name">The Last Straw</div><div class="item-desc">Strawberry ,dates , dairy free ice cream,<br>coconut milk, agave</div><div class="note">*avocado can be substituted with avocado</div></div>
  <div class="item"><div class="item-name">Caffeine Frenzy</div><div class="item-desc">Espresso, banana, dairy free ice cream,<br>cocoa powder, almond milk, agave</div></div>
  <div class="item"><div class="item-name">Berry Bunch</div><div class="item-desc">Oats, mixed berries, banana, dates ,soy milk,<br>dairy free ice cream</div></div>
</section>

<h2 class="abs heading" style="right:74px;top:78px">IMMUNE BOOSTERS</h2>
<div class="band right" style="left:468px;top:111px;width:412px;padding-right:72px">
  <div class="price">REGULAR 16 OZ £6<br>SMOOTHIE BOWL £5.50</div>Available on a seasonal basis
</div>
<section class="abs right" style="right:70px;top:165px;width:360px">
  <div class="item"><div class="item-name">The Yellow One: Pineapple turmeric</div><div class="item-desc">Pineapple, banana, lemon, agave, ginger,<br>tumeric,coconut water</div></div>
  <div class="item"><div class="item-name">The Red One : Citrus Berry Ginger</div><div class="item-desc">Orange, strawberry, lemon, ginger ,<br>almond milk</div></div>
  <div class="item"><div class="item-name">The Orange One : Citrus carrot</div><div class="item-desc">Grapefruit, clementine, carrot,mango,<br>yogurt,lemon,tumeric</div></div>
</section>

<h2 class="abs heading" style="right:74px;top:314px">TEAS</h2>
<div class="band right" style="left:666px;top:346px;width:214px;padding:4px 72px 4px 10px;text-align:center"><span class="price">REGULAR £2</span></div>
<div class="abs plain-list" style="right:74px;top:371px">GREEN GEISHA<br>BREAKFAST BLEND<br>LEMON &amp; GINGER<br>MOROCCAN MINT</div>

<h2 class="abs heading" style="right:74px;top:463px">ICED FRAPPUCINO</h2>
<div class="band" style="left:666px;top:495px;width:214px;padding:4px 72px 4px 10px;text-align:center"><span class="price">REGULAR £4</span></div>
<div class="abs plain-list" style="right:74px;top:519px">CAPPUCCINO <span>- expresso, cream, ice</span><br>COCOA HAZELNUT <span>- hazelnut cocoa ,cream, ice</span><br>STRAWBERRY'S N CREAM<span>- Strawberry,cream,ice</span><br>MIGHTY MATCHA <span>- Matcha, cream, ice</span></div>

<h2 class="abs heading" style="right:74px;top:615px">ZEST SANDWICHES</h2>
<div class="band" style="left:666px;top:646px;width:214px;padding:4px 72px 4px 10px;text-align:center"><span class="price">£4.50</span></div>
<section class="abs right" style="right:70px;top:680px;width:360px">
  <div class="item"><div class="item-name">Avocado</div><div class="item-desc">Avocado , mozerella,tomatoe, pesto</div></div>
  <div class="item"><div class="item-name">Spicy Tuna</div><div class="item-desc">Tuna, Chilli peppers, mayo, salt, pepper</div></div>
  <div class="item"><div class="item-name">Tunacado</div><div class="item-desc">Tuna, avocado, mayo, salt, pepper</div></div>
  <div class="item"><div class="item-name">BLT</div><div class="item-desc">Turkey Rasher, lettuce, mayo, tomatoe</div></div>
  <div class="item"><div class="item-name">American Grilled Cheese</div><div class="item-desc">Mature Cheddar , wholewheat bread</div><div class="note">*sourdough bread is optional</div></div>
</section>

<h2 class="abs heading" style="right:74px;top:873px">YOGURT</h2>
<div class="band" style="left:666px;top:905px;width:214px;padding:4px 72px 4px 10px;text-align:center"><span class="price">£3</span></div>
<div class="abs plain-list" style="right:74px;top:930px;font-weight:500">COCONUT, VANILLA YOGURT, BANANA, GRANOLA</div>

<h2 class="abs heading" style="right:74px;top:963px">BOWLS</h2>
<div class="band" style="left:592px;top:996px;width:288px;padding:4px 72px 4px 10px;text-align:center"><span class="price">£4.50 + PROTEIN=.50P</span></div>
<section class="abs right" style="right:70px;top:1028px;width:360px">
  <div class="item"><div class="item-name">Acai Bowl</div><div class="item-desc">Acai, Raspberry,blueberry,banana,almond milk,<br>granola</div><div class="note">*Topping: granola and ½ banana sliced ,chia seeds</div></div>
  <div class="item"><div class="item-name">Cocoa Bowl</div><div class="item-desc">Cocoa,banana,peanut butter,almond milk</div><div class="note">*almond butter substitute is available</div><div class="item-desc">Toppings : chocolate granola, peanut butter ,chia<br>seeds,1/2 banana sliced</div></div>
</section>
</body>
</html>
```